Roofing Company Sales Rep Business Card

Business card for sales rep to canvass and hand out to property owners/managers for free roof inspections and roof replacements.

```html
<!DOCTYPE html>
<html lang="en">
<head>
<meta charset="utf-8">
<title>Ridgeline Roofing – Sales Representative Card</title>
<link rel="stylesheet" href="https://fonts.googleapis.com/css2?family=League+Spartan:wght@400;600&display=swap">
<style>
  :root {
    --brand-red: #d4120f;
    --card-white: #ffffff;
    --ink: #141414;
  }
  * { margin: 0; padding: 0; box-sizing: border-box; }
  html, body {
    width: 1200px;
    height: 686px;
    overflow: hidden;
    background: var(--card-white);
  }
  .card {
    position: relative;
    width: 1200px;
    height: 686px;
    overflow: hidden;
    background: var(--brand-red);
    font-family: "League Spartan", "Helvetica Neue", Arial, sans-serif;
    color: var(--ink);
  }
  .card__house {
    position: absolute;
    inset: 0;
    width: 1200px;
    height: 686px;
  }
  .contact {
    position: absolute;
    left: 700px;
    top: 60px;
    width: 470px;
    white-space: nowrap;
  }
  .contact__name {
    font-size: 60px;
    font-weight: 400;
    line-height: 1;
    margin-left: 10px;
    letter-spacing: 0.5px;
    text-shadow: 0 3px 6px rgba(0,0,0,0.25);
  }
  .contact__role {
    font-size: 50px;
    font-weight: 400;
    line-height: 1;
    margin-top: 40px;
  }
  .contact__line {
    display: flex;
    align-items: center;
    gap: 4px;
    font-size: 46px;
    font-weight: 400;
    line-height: 1;
  }
  .contact__line--email { margin-top: 14px; }
  .contact__line--phone { margin-top: 24px; }
  .contact__icon { width: 42px; height: 42px; flex: none; }
  .brand {
    position: absolute;
    left: 130px;
    top: 520px;
    display: flex;
    align-items: center;
    gap: 16px;
  }
  .brand__mark {
    width: 30px;
    height: 30px;
    background: var(--ink);
  }
  .brand__name {
    font-size: 56px;
    font-weight: 600;
    letter-spacing: 2px;
    text-transform: uppercase;
    color: var(--ink);
    line-height: 1;
  }
</style>
</head>
<body>
  <main class="card">
    <svg class="card__house" viewBox="0 0 1200 686" aria-hidden="true">
      <polygon fill="var(--card-white)"
        points="71,251 219,251 219,371 409,198 661,429 661,17 1181,17 1181,551 992,666 17,666 17,562 71,509"/>
    </svg>

    <section class="contact">
      <h1 class="contact__name">Sam Carver</h1>
      <p class="contact__role">Sales representative</p>
      <p class="contact__line contact__line--email">
        <svg class="contact__icon" viewBox="0 0 40 40" aria-hidden="true">
          <circle cx="20" cy="20" r="18" fill="var(--ink)"/>
          <rect x="11" y="13" width="18" height="14" rx="1.5" fill="var(--card-white)"/>
          <polyline points="11,14 20,21 29,14" fill="none" stroke="var(--ink)" stroke-width="2"/>
        </svg>
        <span>sam@carverco.com</span>
      </p>
      <p class="contact__line contact__line--phone">
        <svg class="contact__icon" viewBox="0 0 40 40" aria-hidden="true">
          <circle cx="20" cy="20" r="17.5" fill="none" stroke="var(--ink)" stroke-width="2.5"/>
          <path d="M13 11 l4 -1 l3 6 l-3 2 q2 5 6 7 l2 -3 l6 3 l-1 4 q-2 2 -5 1 q-9 -4 -13 -13 q-1 -4 1 -6z" fill="none" stroke="var(--ink)" stroke-width="2" stroke-linejoin="round"/>
        </svg>
        <span>+01 5550148</span>
      </p>
    </section>

    <div class="brand">
      <span class="brand__mark" aria-hidden="true"></span>
      <span class="brand__name">Ridgeline Roofing</span>
    </div>
  </main>
</body>
</html>
```